Template Flyer- Corelune Pilates & Yoga

I am wanting a template 1 page flyer designed to use on the back ground of newsletter (faded background) and for our advertising posters in A4, A3, for Facebook and Instagram compatibility.

I have loaded an example from another Studio called Ferngully (file 3)- each time they have a new workshop to advertise a picture is placed in the little circle (so this is something I would want to do too where I can load a new picture each time a new workshop is running)- They have used the flyer like a water mark...I like this.

Our colour palette is what is on our logos and you can also visit our website for a feel for what we like www.corelunepilates.com.au

I need some of the designs edited a bit more and because of the time difference, there seems to be a 24hour period where we communicate with each other. May I please request another 2 days extension

Need extra days to review

Requirements
Must have
• Id like to have a picture in the back ground. My favourite back ground that has been produced so far is a background of both picture file 9 and 10 in either.
Nice to have
• 3 picture circles options to advertise the events/workshops I have each year.
• Brush stroke style circles (see picture attached)rather then smooth circles for the picture area (in a grey tone)
Should not have
• No BLACK colour writing or black circles

```html
<!DOCTYPE html>
<html lang="en">
<head>
<meta charset="utf-8">
<title>Corelune Pilates &amp; Yoga – Workshop Flyer</title>
<link href="https://fonts.googleapis.com/css2?family=Montserrat:wght@300;400;500;700;800&display=swap" rel="stylesheet">
<style>
  :root {
    --teal: #2a8fad;
    --slate-teal: #245565;
    --stone: #b7afa6;
    --wall-light: #fafafa;
    --wall-mid: #e4e4e2;
    --wall-shade: #d6d6d3;
    --photo-a: #d9e6ea;
    --photo-b: #8fc3d3;
    --photo-c: #e9dcc4;
  }
  * { box-sizing: border-box; margin: 0; padding: 0; }
  html, body { width: 1200px; height: 1200px; overflow: hidden; }
  body {
    font-family: "Montserrat", sans-serif;
    background: #ffffff;
    position: relative;
  }
  .flyer {
    position: absolute; inset: 0;
    width: 1200px; height: 1200px;
    overflow: hidden;
  }
  .backdrop {
    position: absolute; inset: 0;
    background:
      radial-gradient(ellipse 70px 14px at 250px 40px, #ffffff, rgba(255,255,255,0) 100%),
      radial-gradient(ellipse 70px 14px at 600px 40px, #ffffff, rgba(255,255,255,0) 100%),
      radial-gradient(ellipse 70px 14px at 955px 40px, #ffffff, rgba(255,255,255,0) 100%),
      radial-gradient(ellipse 230px 480px at 250px 260px, rgba(255,255,255,.95), rgba(255,255,255,0) 75%),
      radial-gradient(ellipse 230px 480px at 600px 260px, rgba(255,255,255,.95), rgba(255,255,255,0) 75%),
      radial-gradient(ellipse 230px 480px at 955px 260px, rgba(255,255,255,.95), rgba(255,255,255,0) 75%),
      linear-gradient(180deg, var(--wall-shade) 0%, var(--wall-mid) 14%, var(--wall-light) 40%, #ededeb 80%, #f7f7f7 90%, #ffffff 100%);
  }
  .backdrop__vignette {
    position: absolute; inset: 0;
    background: linear-gradient(90deg, rgba(200,200,197,.55) 0%, rgba(255,255,255,0) 18%, rgba(255,255,255,0) 82%, rgba(200,200,197,.55) 100%);
  }
  .feature {
    position: absolute; left: 0; top: 0;
    width: 1200px; height: 720px;
  }
  .headline {
    position: absolute; left: 0; right: 0; top: 725px;
    text-align: center; color: var(--teal);
    line-height: 1.12;
  }
  .headline__lead { font-weight: 400; font-size: 55px; letter-spacing: .3px; display: block; }
  .headline__strong { font-weight: 800; font-size: 54px; display: block; }
  .details {
    position: absolute; left: 0; right: 0; top: 872px;
    text-align: center;
  }
  .details p { line-height: 40px; }
  .details__address, .details__email { color: var(--slate-teal); font-weight: 500; font-size: 25px; }
  .details__hours, .details__phone { color: var(--teal); font-weight: 700; font-size: 31px; letter-spacing: -.3px; }
  .footer {
    position: absolute; left: 0; right: 0; bottom: 0; height: 150px;
    background: linear-gradient(180deg, rgba(255,255,255,0) 0%, #ffffff 30%);
  }
  .brand {
    position: absolute; left: 36px; top: 46px;
    display: flex; align-items: center; gap: 14px;
  }
  .brand__mark {
    width: 62px; height: 62px; border-radius: 50%;
    border: 4px solid var(--teal);
  }
  .brand__name {
    font-weight: 400; font-size: 36px; color: var(--teal); letter-spacing: -.3px;
  }
  .social {
    position: absolute; right: 54px; top: 50px;
    display: flex; gap: 17px;
  }
  .social__item {
    width: 54px; height: 54px; border-radius: 50%;
    background: var(--teal);
    display: flex; align-items: center; justify-content: center;
  }
</style>
</head>
<body>
<main class="flyer">
  <div class="backdrop" role="img" aria-label="Background photo: softly lit white painted brick studio wall under three ceiling lights">
    <div class="backdrop__vignette"></div>
  </div>

  <svg class="feature" viewBox="0 0 1200 720">
    <defs>
      <linearGradient id="photoTone" x1="0" y1="0" x2="1" y2="1">
        <stop offset="0" stop-color="var(--photo-a)"/>
        <stop offset=".45" stop-color="var(--photo-b)"/>
        <stop offset="1" stop-color="var(--photo-c)"/>
      </linearGradient>
    </defs>
    <circle class="feature__ring-teal" cx="600" cy="392" r="308" fill="var(--teal)"/>
    <circle class="feature__ring-stone" cx="622" cy="382" r="288" fill="var(--stone)"/>
    <circle class="feature__photo" cx="606" cy="385" r="280" fill="url(#photoTone)"
            role="img" aria-label="Workshop photo: pile of patterned fabric yoga bolsters in blue, lime, grey and peach"/>
  </svg>

  <h1 class="headline">
    <span class="headline__lead">PILATES AND YOGA FOR</span>
    <span class="headline__strong">YOUR MIND, BODY &amp; SOUL.</span>
  </h1>

  <section class="details">
    <p class="details__address">18 Wattlebrook Lane, Hollowmere, VIC 3499</p>
    <p class="details__hours">MON – SUN, 6.15AM – 9.00PM (DURING CLASS HOURS)</p>
    <p class="details__phone">(03) 5550 1842</p>
    <p class="details__email">info@corelunepilates.com.au</p>
  </section>

  <footer class="footer">
    <div class="brand">
      <span class="brand__mark"></span>
      <span class="brand__name">Corelune Pilates &amp; Yoga</span>
    </div>
    <div class="social">
      <span class="social__item" aria-label="Social link"></span>
      <span class="social__item" aria-label="Social link"></span>
      <span class="social__item" aria-label="Email">
        <svg width="26" height="20" viewBox="0 0 26 20" fill="none" stroke="#fff" stroke-width="2.4" stroke-linejoin="round">
          <rect x="1.5" y="1.5" width="23" height="17" rx="2"/>
          <path d="M2 3l11 8 11-8"/>
        </svg>
      </span>
      <span class="social__item" aria-label="Social link"></span>
    </div>
  </footer>
</main>
</body>
</html>
```